Attention grabbing 6x9 postcard

We are looking to have an attention grabbing post card that be sent out to homeowners from our roofing company Olum Roofing. the concept is that on the front it will say something like (STOP THE KNOCKING!
Tired of roofers knocking on your door? Contact us because we value your time as much as you value the roof over your head."
Olum Roofing
OlumRoofing.com
877.612.OLUM
info@olumroofing.com

Please feel free to come up with something very creative. Once we pick the final design we will provide the copy.

```html
<!DOCTYPE html>
<html lang="en">
<head>
<meta charset="utf-8">
<title>Olum Roofing Postcard</title>
<link href="https://fonts.googleapis.com/css2?family=Barlow+Condensed:wght@400;500;700;800&family=Montserrat:wght@700&display=swap" rel="stylesheet">
<style>
  :root {
    --honey: #e6b335;
    --ink: #1b1d20;
    --page: #ece9e4;
    --sky: #7fb6e6;
    --tile: #3b4a5a;
    --work: #6f6d63;
  }
  * { margin: 0; padding: 0; box-sizing: border-box; }
  html, body { width: 1200px; height: 1200px; overflow: hidden; background: var(--page); }
  body { position: relative; font-family: "Barlow Condensed", sans-serif; color: var(--ink); }

  .postcard {
    position: absolute; left: 195px; width: 900px; height: 600px;
    background: var(--honey); overflow: hidden;
    transform: scale(0.9); transform-origin: top left;
    box-shadow: 0 3px 10px rgba(0,0,0,0.12);
  }
  .postcard--front { top: 45px; }
  .postcard--back { top: 615px; }
  .shapes { position: absolute; inset: 0; width: 900px; height: 600px; }

  .brand {
    position: absolute; display: flex; align-items: center; gap: 8px;
    font-family: "Montserrat", sans-serif; font-weight: 700;
    font-size: 13px; letter-spacing: 2.5px; color: var(--ink);
  }
  .brand__dot { width: 12px; height: 12px; border-radius: 50%; background: var(--ink); }
  .postcard--front .brand { right: 36px; top: 118px; }
  .postcard--back .brand { left: 570px; top: 102px; }

  .headline {
    position: absolute; right: 38px; top: 318px; text-align: right;
    font-weight: 800; font-size: 64px; line-height: 58px; color: var(--honey);
    text-transform: uppercase;
  }
  .pitch {
    position: absolute; right: 38px; top: 504px; width: 300px; text-align: justify;
    text-align-last: right; font-size: 14px; line-height: 18px; color: var(--honey);
    text-transform: uppercase;
  }
  .contact-row {
    position: absolute; left: 38px; top: 536px; display: flex; gap: 16px;
    font-size: 16px; text-transform: uppercase; color: var(--ink);
  }
  .contact-row span { display: flex; align-items: center; gap: 5px; }
  .contact-row svg { width: 12px; height: 12px; }

  .why {
    position: absolute; right: 412px; top: 36px; text-align: right;
    font-weight: 800; font-size: 44px; line-height: 42px; text-transform: uppercase;
  }
  .benefits { position: absolute; left: 38px; top: 348px; list-style: none; }
  .benefits li {
    display: flex; align-items: center; gap: 14px; height: 54px;
    font-size: 15px; text-transform: uppercase;
  }
  .benefits b { font-weight: 700; }
  .benefits svg { width: 38px; height: 40px; flex: none; }

  .web {
    position: absolute; left: 568px; top: 486px; font-weight: 800; font-size: 40px;
    line-height: 40px; text-transform: uppercase;
  }
  .phone { position: absolute; left: 570px; top: 530px; font-size: 28px; font-weight: 500; }
</style>
</head>
<body>

<section class="postcard postcard--front">
  <svg class="shapes" viewBox="0 0 900 600" aria-hidden="true">
    <polygon points="0,0 100,0 100,238 0,296" fill="var(--ink)"/>
    <polygon points="512,300 735,178 900,268 900,600 560,600 512,555" fill="var(--ink)"/>
  </svg>
  <svg class="shapes" viewBox="0 0 900 600" role="img" aria-label="Photo of a tiled roof with a gable under a clear blue sky">
    <defs>
      <linearGradient id="roofPhoto" x1="0" y1="0" x2="0" y2="1">
        <stop offset="0" stop-color="var(--sky)"/>
        <stop offset="0.4" stop-color="#a9cdea"/>
        <stop offset="0.45" stop-color="var(--tile)"/>
        <stop offset="1" stop-color="#2a3038"/>
      </linearGradient>
    </defs>
    <polygon points="308,37 512,155 512,385 308,510 100,385 100,150" fill="url(#roofPhoto)"/>
  </svg>
  <div class="brand"><span class="brand__dot"></span>OLUM ROOFING</div>
  <h1 class="headline">Stop<br>the<br>Knocking!</h1>
  <p class="pitch">Tired of roofers knocking on your door? Contact us because we value your time as much as you value the roof over your head.</p>
  <div class="contact-row">
    <span><svg viewBox="0 0 12 12"><polygon points="6,1 10.5,3.5 10.5,8.5 6,11 1.5,8.5 1.5,3.5" fill="none" stroke="var(--ink)" stroke-width="1.6"/></svg>OlumRoofing.com</span>
    <span><svg viewBox="0 0 12 12"><polygon points="6,1 10.5,3.5 10.5,8.5 6,11 1.5,8.5 1.5,3.5" fill="none" stroke="var(--ink)" stroke-width="1.6"/></svg>877.612.OLUM</span>
    <span><svg viewBox="0 0 12 12"><polygon points="6,1 10.5,3.5 10.5,8.5 6,11 1.5,8.5 1.5,3.5" fill="none" stroke="var(--ink)" stroke-width="1.6"/></svg>info@olumroofing.com</span>
  </div>
</section>

<section class="postcard postcard--back">
  <svg class="shapes" viewBox="0 0 900 600" role="img" aria-label="Photo of a roofer nailing asphalt shingles with a nail gun">
    <defs>
      <linearGradient id="workPhoto" x1="0" y1="0" x2="1" y2="1">
        <stop offset="0" stop-color="#4b5560"/>
        <stop offset="0.5" stop-color="var(--work)"/>
        <stop offset="1" stop-color="#8b8a84"/>
      </linearGradient>
    </defs>
    <polygon points="0,0 312,0 312,232 140,335 0,262" fill="url(#workPhoto)"/>
  </svg>
  <svg class="shapes" viewBox="0 0 900 600" aria-hidden="true">
    <line x1="528" y1="6" x2="528" y2="596" stroke="var(--ink)" stroke-width="4" stroke-dasharray="0 9" stroke-linecap="round"/>
    <rect x="733" y="40" width="125" height="150" fill="none" stroke="var(--ink)" stroke-width="1.5"/>
    <g stroke="var(--ink)" stroke-width="1.2">
      <line x1="570" y1="247" x2="858" y2="247"/>
      <line x1="570" y1="307" x2="858" y2="307"/>
      <line x1="570" y1="365" x2="858" y2="365"/>
      <line x1="570" y1="422" x2="858" y2="422"/>
    </g>
  </svg>
  <h2 class="why">Why<br>Choose<br>Us?</h2>
  <ul class="benefits">
    <li><svg viewBox="0 0 38 40"><polygon points="19,1 36,10 36,30 19,39 2,30 2,10" fill="var(--ink)"/><polyline points="10,20 17,27 29,13" fill="none" stroke="var(--honey)" stroke-width="4"/></svg><span><b>Durable Materials</b> - Built to last in any weather</span></li>
    <li><svg viewBox="0 0 38 40"><polygon points="19,1 36,10 36,30 19,39 2,30 2,10" fill="var(--ink)"/><polyline points="10,20 17,27 29,13" fill="none" stroke="var(--honey)" stroke-width="4"/></svg><span><b>Experienced Team</b> - Years of industry expertise</span></li>
    <li><svg viewBox="0 0 38 40"><polygon points="19,1 36,10 36,30 19,39 2,30 2,10" fill="var(--ink)"/><polyline points="10,20 17,27 29,13" fill="none" stroke="var(--honey)" stroke-width="4"/></svg><span><b>Affordable Pricing</b> - Quality service at competitive rates</span></li>
    <li><svg viewBox="0 0 38 40"><polygon points="19,1 36,10 36,30 19,39 2,30 2,10" fill="var(--ink)"/><polyline points="10,20 17,27 29,13" fill="none" stroke="var(--honey)" stroke-width="4"/></svg><span><b>Quick Turnaround</b> - Fast and efficient service</span></li>
  </ul>
  <div class="brand"><span class="brand__dot"></span>OLUM ROOFING</div>
  <p class="web">OlumRoofing.com</p>
  <p class="phone">877.612.OLUM</p>
</section>

</body>
</html>
```